The Harrowgate Ledger Summit. A Summit For Ledger Keepers...By Ledger Keepers.
The Harrowgate Ledger Summit was created to provide quality content at a reasonable price-point to allow organizations to send multiple attendees and encourage active participation. This event is intended for debt collection professionals who are:

Senior Level Executives
Front Line Collection Managers
Compliance Professionals
Trainers
While there are many great conferences within our industry to choose from, most collection conferences just scratch the surface when attempting to provide real world solutions. The Harrowgate Ledger Summit was created to provide debt collection professionals with a foundation of direction, insight, and actionable solutions that can be applied regardless of the size of an organization. Join us at the inaugural Harrowgate Ledger Summit as we assemble an expert team of operations, compliance, and training professionals that will deep dive into real world solutions for today’s real world debt collection issues. Here is what you can expect:

Solution driven sessions, not sponsor driven sessions
Substance from "In The Trenches" experts who live it, breathe it, work it...every day
Learn operational, compliance, and training strategies that have proven success
Understand how to efficiently and effectively manage YOUR resources
Apply state of the art technology solutions

Target Market(s)

Debt collection agencies and creditors

Industry/Entity Type

Financial Service

Font styles to use
Serif

Requirements
Must have
• link to website www.HLS2016.example and use of image provided HLSCover. Use same color scheme as the HLSCover image

```html
<!DOCTYPE html>
<html lang="en">
<head>
<meta charset="utf-8">
<title>Harrowgate Ledger Summit 2016 – Cover and Flyer</title>
<link rel="stylesheet" href="https://fonts.googleapis.com/css2?family=Roboto+Condensed:wght@300&family=Carlito:wght@400;700&family=Arimo:wght@700&display=swap">
<style>
  :root {
    --backdrop: #e4e4e4;
    --paper: #ffffff;
    --teal: #2bb3c4;
    --teal-glow: rgba(32, 196, 212, 0.85);
    --teal-deep: #1f9aab;
    --lime: #c4cc3a;
    --lime-glow: rgba(196, 204, 58, 0.85);
    --ink: #3a3a3a;
    --muted: #8a8a8a;
    --photo-light: #c9c9c9;
    --photo-mid: #7d7d7d;
    --photo-dark: #2e2e2e;
    --frame: #111111;
  }

  * { box-sizing: border-box; margin: 0; padding: 0; }

  html, body {
    width: 1200px;
    height: 803px;
    overflow: hidden;
    background: var(--backdrop);
  }

  .spread { position: relative; width: 1200px; height: 803px; }

  .page {
    position: absolute;
    top: 40px;
    width: 500px;
    height: 723px;
    background: var(--paper);
    overflow: hidden;
  }

  /* ---------- Cover ---------- */
  .cover { left: 60px; }

  .cover-photo {
    position: absolute;
    inset: 0;
    background:
      radial-gradient(ellipse 300px 340px at 60px 160px, var(--teal-glow) 0%, rgba(32,196,212,0.55) 55%, rgba(32,196,212,0) 100%),
      radial-gradient(ellipse 320px 300px at 90px 560px, var(--lime-glow) 0%, rgba(196,204,58,0.5) 55%, rgba(196,204,58,0) 100%),
      linear-gradient(180deg,
        var(--photo-mid) 0%,
        #a9a9a9 22%,
        #9a9a9a 45%,
        #5e5e5e 55%,
        #474747 70%,
        var(--photo-dark) 100%);
  }

  .cover-lockup {
    position: absolute;
    left: 198px;
    top: 508px;
    display: flex;
    align-items: flex-start;
    gap: 14px;
  }

  .brand-square {
    width: 40px;
    height: 40px;
    background: var(--teal);
    flex: none;
    margin-top: 6px;
  }

  .brand-name {
    font-family: "Roboto Condensed", sans-serif;
    font-weight: 300;
    color: #ffffff;
    text-transform: uppercase;
    letter-spacing: 3px;
    font-size: 25px;
    line-height: 1.2;
    border-left: 1px solid rgba(255,255,255,0.7);
    padding-left: 12px;
  }

  .cover-tagline {
    position: absolute;
    left: 260px;
    top: 626px;
    font-family: "Arimo", sans-serif;
    font-weight: 700;
    font-size: 8.5px;
    color: #ffffff;
  }

  .cover-event {
    position: absolute;
    left: 262px;
    top: 656px;
    font-family: "Arimo", sans-serif;
    font-weight: 700;
    font-size: 12px;
    line-height: 1.35;
    color: #ffffff;
    text-transform: uppercase;
  }

  /* ---------- Flyer ---------- */
  .flyer { left: 640px; }

  .flyer-banner {
    position: absolute;
    left: 18px;
    top: 14px;
    width: 464px;
    height: 136px;
    background:
      linear-gradient(90deg, rgba(43,179,196,0.35) 0%, rgba(196,204,58,0.25) 8%, rgba(0,0,0,0) 14%),
      linear-gradient(90deg, #e2e2e2 0%, #c4c4c4 35%, #8d8d8d 60%, #5a5a5a 100%);
  }

  .banner-lockup {
    position: absolute;
    left: 30px;
    top: 26px;
    display: flex;
    gap: 12px;
    align-items: flex-start;
  }
  .banner-lockup .brand-square { width: 28px; height: 28px; margin-top: 4px; }
  .banner-lockup .brand-name {
    color: var(--ink);
    font-size: 19px;
    letter-spacing: 2.5px;
    border-left-color: var(--ink);
  }
  .banner-tagline {
    position: absolute;
    left: 70px;
    top: 106px;
    font-family: "Arimo", sans-serif;
    font-weight: 700;
    font-size: 7.5px;
    color: var(--ink);
  }

  .flyer-body {
    position: absolute;
    left: 26px;
    right: 26px;
    top: 164px;
    font-family: "Carlito", sans-serif;
    font-size: 10.5px;
    line-height: 1.38;
    color: var(--ink);
  }

  .flyer-heading {
    text-align: center;
    color: var(--teal-deep);
    font-family: "Carlito", sans-serif;
    font-weight: 400;
    font-size: 12.5px;
    line-height: 1.3;
    text-transform: uppercase;
    letter-spacing: 0.3px;
    margin-bottom: 18px;
  }

  .flyer-body p { text-align: justify; margin-bottom: 14px; }

  .tick-list { list-style: none; margin-bottom: 14px; }
  .tick-list li { position: relative; padding-left: 13px; }
  .tick-list li svg {
    position: absolute;
    left: 0;
    top: 3px;
    width: 9px;
    height: 8px;
  }

  .event-photo {
    position: absolute;
    border: 4px solid var(--frame);
    background: linear-gradient(180deg,
      #d9d2c4 0%, #b8aa94 35%, #7a6a5a 60%, #5c4a44 100%);
  }
  .event-photo.wide {
    left: 22px;
    top: 556px;
    width: 246px;
    height: 134px;
  }
  .event-photo.tilted {
    left: 298px;
    top: 546px;
    width: 170px;
    height: 126px;
    transform: rotate(4deg);
  }

  .flyer-footer {
    position: absolute;
    left: 18px;
    right: 18px;
    bottom: 10px;
  }
  .flyer-footer .contact {
    text-align: right;
    font-family: "Arimo", sans-serif;
    font-weight: 700;
    font-size: 7px;
    color: var(--muted);
    margin-bottom: 4px;
  }
  .footer-rule { height: 1px; background: var(--teal); margin-bottom: 2px; }
  .footer-rule.lime { background: var(--lime); }
</style>
</head>
<body>
<main class="spread">

  <section class="page cover" aria-label="Event cover">
    <div class="cover-photo" role="img" aria-label="Black and white photograph of the Saint Louis riverfront skyline with the Gateway Arch over the river and rocks in the foreground, washed with teal and lime light"></div>

    <div class="cover-lockup">
      <span class="brand-square" aria-hidden="true"></span>
      <h1 class="brand-name">Harrowgate<br>Ledger<br>Summit 2016</h1>
    </div>
    <p class="cover-tagline">A Summit for ledger keepers... by ledger keepers.</p>
    <p class="cover-event">Saint Louis, Missouri<br>March 21, 2016 - March 23, 2016</p>
  </section>

  <section class="page flyer" aria-label="Event information flyer">
    <div class="flyer-banner" role="img" aria-label="Black and white riverfront skyline with the Gateway Arch">
      <div class="banner-lockup">
        <span class="brand-square" aria-hidden="true"></span>
        <span class="brand-name">Harrowgate<br>Ledger<br>Summit 2016</span>
      </div>
      <p class="banner-tagline">A Summit for ledger keepers... by ledger keepers.</p>
    </div>

    <div class="flyer-body">
      <h2 class="flyer-heading">The Harrowgate Ledger Summit<br>A Summit for Ledger Keepers...By Ledger Keepers.</h2>

      <p>The Harrowgate Ledger Summit was created to provide quality content at a reasonable price-point to allow organizations to send multiple attendees and encourage active participation. This event is intended for debt collection professionals who are:</p>

      <ul class="tick-list">
        <li><svg viewBox="0 0 9 8" aria-hidden="true"><path d="M1 4.2 L3.4 6.6 L8 1" fill="none" stroke="var(--teal)" stroke-width="1.5"/></svg>Senior Level Executives</li>
        <li><svg viewBox="0 0 9 8" aria-hidden="true"><path d="M1 4.2 L3.4 6.6 L8 1" fill="none" stroke="var(--teal)" stroke-width="1.5"/></svg>Front Line Collection Managers</li>
        <li><svg viewBox="0 0 9 8" aria-hidden="true"><path d="M1 4.2 L3.4 6.6 L8 1" fill="none" stroke="var(--teal)" stroke-width="1.5"/></svg>Compliance Professionals</li>
        <li><svg viewBox="0 0 9 8" aria-hidden="true"><path d="M1 4.2 L3.4 6.6 L8 1" fill="none" stroke="var(--teal)" stroke-width="1.5"/></svg>Trainers</li>
      </ul>

      <p>While there are many great conferences within our industry to choose from, most collection conferences just scratch the surface when attempting to provide real world solutions. The Harrowgate Ledger Summit was created to provide debt collection professionals with a foundation of direction, insight, and actionable solutions that can be applied regardless of the size of an organization. Join us at the inaugural Harrowgate Ledger Summit as we assemble an expert team of operations, compliance, and training professionals that will deep dive into real world solutions for today’s real world debt collection issues. Here is what you can expect:</p>

      <ul class="tick-list">
        <li><svg viewBox="0 0 9 8" aria-hidden="true"><path d="M1 4.2 L3.4 6.6 L8 1" fill="none" stroke="var(--teal)" stroke-width="1.5"/></svg>Solution driven sessions, not sponsor driven sessions</li>
        <li><svg viewBox="0 0 9 8" aria-hidden="true"><path d="M1 4.2 L3.4 6.6 L8 1" fill="none" stroke="var(--teal)" stroke-width="1.5"/></svg>Substance from "In The Trenches" experts who live it, breathe it, work it...every day</li>
        <li><svg viewBox="0 0 9 8" aria-hidden="true"><path d="M1 4.2 L3.4 6.6 L8 1" fill="none" stroke="var(--teal)" stroke-width="1.5"/></svg>Learn operational, compliance, and training strategies that have proven results</li>
        <li><svg viewBox="0 0 9 8" aria-hidden="true"><path d="M1 4.2 L3.4 6.6 L8 1" fill="none" stroke="var(--teal)" stroke-width="1.5"/></svg>Understand how to efficiently and effectively manage YOUR resources</li>
        <li><svg viewBox="0 0 9 8" aria-hidden="true"><path d="M1 4.2 L3.4 6.6 L8 1" fill="none" stroke="var(--teal)" stroke-width="1.5"/></svg>Apply state of the art technology solutions</li>
      </ul>
    </div>

    <div class="event-photo wide" role="img" aria-label="Wide view of a conference ballroom with attendees seated at round tables facing projection screens"></div>
    <div class="event-photo tilted" role="img" aria-label="Conference session with attendees at tables and a presentation on screens"></div>

    <footer class="flyer-footer">
      <p class="contact">555-014-2016 &nbsp;|&nbsp; www.HLS2016.example &nbsp;|&nbsp; info@hls2016.example</p>
      <div class="footer-rule"></div>
      <div class="footer-rule lime"></div>
    </footer>
  </section>

</main>
</body>
</html>
```